Small environmental consultancy needs a simple but professional web design

We are a boutique environmental consultancyand contracting business located in Margaret River in the South West of Western Australia.

We have two arms
1) Consulting which offers environmental planning, management and assessment services primarily to local government and the development industry.
2) Contracting which implements on site plans and on ground works primarily involving revegetation, bush regeneration and environmental weed control.

We need a simple yet professional web design within the wordpress platform that commmunicates professionalism, experience and technical expertise without appearing too corporate.

Something like this structure appeals:
http://tarnwick.net.au/environment-services/
or
http://www.brackleyfieldworks.com.au/index.php

(without the image gallery function)

Target Market(s)

Local Government Officers deciding on tenders;
Developers, Engineers, Town Planning consultants looking for environmental expertise

Industry/Entity Type

Business

Number of Pages Required

5+ page

Font styles to use
Sans Serif

Colors
33a6d7
9bcb3c

Requirements
Must have
• Pages required include:
• Home
• Environmental Planning and Management
• Revegetation and Regeneration Implementation (This page can mirror the Environmental Planning and Management page exactly in structure but with different text and images)
• About Us (I think that this page can be relatively simple and generic)
• Contact (I think that this page can be very simple and generic)
Nice to have
• An ability to start out basic and quicikly establish a website presence and then build in additional drop downs and pages over time.
Should not have
• It does not need a photo gallery page;
• It does not need a major amount of space dedicated to social media and blogs etc as this is not currently particularly active area for us

```html
<!DOCTYPE html>
<html lang="en">
<head>
<meta charset="utf-8">
<title>Marri Vale Ecoservices</title>
<link href="https://fonts.googleapis.com/css2?family=Roboto:wght@300;400;500;700&display=swap" rel="stylesheet">
<style>
:root{
  --green:#9bcb3c;
  --blue:#33a6d7;
  --dark:#222222;
  --darker:#1b1b1b;
  --grey-bg:#f0f0f0;
  --text:#8a8a8a;
  --heading:#333333;
  --white:#ffffff;
}
*{box-sizing:border-box;margin:0;padding:0}
html,body{width:676px;height:1200px;overflow:hidden;background:var(--white)}
body{position:relative;font-family:'Roboto',sans-serif;color:var(--text)}
.abs{position:absolute}

/* header */
.brand{left:96px;top:8px;height:62px;display:flex;align-items:center;gap:10px}
.brand-mark{width:44px;height:44px;border-radius:50%;background:var(--green);flex:none}
.brand-name{font-size:19px;font-weight:500;color:var(--green);white-space:nowrap}
.main-nav{right:96px;top:34px;display:flex;font-size:10px;color:#555;text-transform:uppercase;letter-spacing:.3px}
.main-nav span{padding:0 11px;border-left:1px solid #ddd}
.main-nav span:first-child{border-left:none}
.tab{top:76px;height:23px;width:230px;font-size:7.8px;font-weight:700;color:var(--white);display:flex;align-items:center;justify-content:center;text-transform:uppercase;border-radius:2px 2px 0 0;white-space:nowrap;letter-spacing:-.1px}
.tab-green{left:96px;background:var(--green)}
.tab-blue{left:355px;background:var(--blue)}

/* hero */
.hero{left:0;top:98px;width:676px;height:222px;border-top:3px solid var(--dark);
  background:linear-gradient(90deg,#c9a9a6 0%,#b95a84 18%,#d8b9b9 36%,#8a8f5c 50%,#e4562b 62%,#f0a24a 72%,#7d8d55 86%,#b9bfa5 100%)}
.hero-arrow{left:29px;top:205px;width:26px;height:26px;border:1.5px solid rgba(255,255,255,.8);border-radius:50%}
.hero-caption{left:96px;top:266px;width:489px;height:38px;background:rgba(30,30,30,.78);color:var(--white);font-size:12px;font-weight:300;text-align:center;padding-top:8px}
.dots{left:314px;top:291px;display:flex;gap:3px}
.dots i{width:6px;height:6px;border-radius:50%;border:1px solid var(--green);display:block}
.dots i.on{background:var(--white);border-color:var(--white)}

/* welcome */
.welcome{left:0;top:320px;width:676px;height:85px;background:var(--dark);text-align:center}
.welcome h1{margin-top:15px;font-size:21px;font-weight:300;color:var(--white);letter-spacing:.3px}
.welcome h1 em{font-style:normal;color:var(--green)}
.welcome p{margin:7px auto 0;width:560px;font-size:7.8px;line-height:13px;color:#b4b4b4}
.pointer{left:320px;top:404px}

/* why us */
.section-title{font-size:21px;font-weight:300;color:var(--heading);letter-spacing:.3px}
.why-title{left:0;width:676px;top:446px;text-align:center}
.feature{top:506px;width:126px;text-align:center}
.feature-icon{width:64px;height:64px;margin:0 auto;border-radius:50%;border:3px solid var(--green);background:var(--white);display:flex;align-items:center;justify-content:center}
.feature-icon span{width:52px;height:52px;border-radius:50%;background:var(--green);display:flex;align-items:center;justify-content:center}
.feature h3{margin-top:19px;font-size:9px;font-weight:700;color:var(--heading);line-height:12px;text-transform:uppercase}
.feature p{margin-top:6px;font-size:8px;line-height:12px;color:#9a9a9a}

/* grey band */
.band{left:0;top:672px;width:676px;height:392px;background:var(--grey-bg)}
.about-title{left:75px;top:716px}
.more-btn{left:262px;top:725px;width:30px;height:12px;background:var(--blue);color:var(--white);font-size:6.5px;display:flex;align-items:center;justify-content:center;border-radius:1px}
.about-text{left:75px;top:772px;width:228px;font-size:8px;line-height:11.5px;color:#9a9a9a}
.about-text p{margin-bottom:11px}
.about-photo{left:75px;top:938px;width:228px;height:96px;background:linear-gradient(135deg,#3f5a22,#7f9a4a 45%,#e9e6e0 55%,#4c6a2a)}
.projects-title{left:372px;top:716px}
.project{left:372px;width:250px;display:flex;gap:14px;align-items:center}
.project-photo{width:91px;height:66px;border:3px solid var(--white);flex:none}
.project p{font-size:8.8px;line-height:12px;color:#444}

/* footer */
.footer{left:0;top:1064px;width:676px;height:136px;background:var(--darker)}
.footer-brand{left:68px;top:1094px;width:140px;text-align:center}
.footer-brand .brand-mark{width:34px;height:34px;margin:0 auto 14px}
.footer-brand .name{font-size:11.5px;font-weight:500;color:var(--green);white-space:nowrap}
.copyright{left:83px;top:1173px;font-size:6.8px;color:#aaa}
.f-col{top:1085px}
.f-col h4{font-size:10px;font-weight:400;color:var(--green);margin-bottom:10px}
.f-col li{list-style:none;font-size:7px;line-height:13px;color:#aaa}
.f-col .info{font-size:7px;line-height:10px;color:#ccc;margin-bottom:10px}
.f-col .info b{color:var(--white);font-weight:700}
</style>
</head>
<body>

<header>
  <div class="abs brand"><span class="brand-mark"></span><span class="brand-name">Marri Vale Ecoservices</span></div>
  <nav class="abs main-nav"><span>Home</span><span>About Us</span><span>Contact</span></nav>
  <div class="abs tab tab-green">Environmental Planning and Management</div>
  <div class="abs tab tab-blue">Revegetation and Regeneration Implementation</div>
</header>

<section class="abs hero" role="img" aria-label="Slider photo of native orchid and red banksia-like wildflowers"></section>
<div class="abs hero-arrow"><svg width="23" height="23" viewBox="0 0 23 23"><path d="M13 7l-5 4.5 5 4.5" fill="none" stroke="#fff" stroke-width="1.5"/></svg></div>
<div class="abs hero-caption">Positive Outcomes for People, Projects, and the Environment</div>
<div class="abs dots"><i></i><i></i><i class="on"></i><i></i><i></i></div>

<section class="abs welcome">
  <h1>WELCOME TO <em>MARRI VALE ECOSERVICES</em></h1>
  <p>We are a specialist botanical consultancy with more than 15 years of experience providing professional services that our clients trust and rely on. Our committed employees located throughout Western Australia, bring inter-disciplinary expertise to every project we work on. Our clients look to us to</p>
</section>
<svg class="abs pointer" width="36" height="20" viewBox="0 0 36 20"><path d="M0 0h36L18 19z" fill="#222"/></svg>

<h2 class="abs section-title why-title">WHY US?</h2>
<svg class="abs" style="left:308px;top:479px" width="60" height="6" viewBox="0 0 60 6"><path d="M0 3h20M40 3h20" stroke="#33a6d7" stroke-width="1.5"/><path d="M22 5l4-4M27 5l4-4M32 5l4-4" stroke="#33a6d7" stroke-width="1"/></svg>

<div class="abs feature" style="left:70px">
  <div class="feature-icon"><span><svg width="30" height="30" viewBox="0 0 30 30" fill="none" stroke="#111" stroke-width="2"><circle cx="15" cy="15" r="12"/><path d="M3 15h24M15 3v24M7 7l16 16"/></svg></span></div>
  <h3>GIS Mapping and<br>Analysis</h3>
  <p>Lorem ipsum dolor sit amet, consectetur adipiscing elit, sed do eiusmod tempor incididunt</p>
</div>
<div class="abs feature" style="left:208px">
  <div class="feature-icon"><span><svg width="30" height="30" viewBox="0 0 30 30"><path d="M15 16c0-6 4-9 8-9-1 5-4 8-8 9zM15 16c0-5-3-7-7-7 1 4 3 6 7 7z" fill="#111"/><path d="M4 22c4-2 8-2 11 0h8c1 0 1 2 0 2H8z" fill="#111"/></svg></span></div>
  <h3>Enviornmental<br>Impact Assessment</h3>
  <p>Sed ut perspiciatis unde omnis iste natus error sit voluptatem accusantium doloremque</p>
</div>
<div class="abs feature" style="left:342px">
  <div class="feature-icon"><span><svg width="30" height="30" viewBox="0 0 30 30" fill="#111"><rect x="13" y="4" width="5" height="22" rx="2.5"/><rect x="7" y="10" width="4" height="9" rx="2"/><rect x="7" y="16" width="7" height="3"/><rect x="20" y="8" width="4" height="9" rx="2"/><rect x="17" y="14" width="7" height="3"/></svg></span></div>
  <h3>Native Vegetation<br>Clearing Permits</h3>
  <p>I must explain to you how all this mistaken idea of denouncing pleasure and</p>
</div>
<div class="abs feature" style="left:479px">
  <div class="feature-icon"><span><svg width="32" height="30" viewBox="0 0 32 30" fill="#111"><rect x="7" y="12" width="2" height="14"/><rect x="15" y="9" width="2" height="17"/><rect x="23" y="12" width="2" height="14"/><circle cx="8" cy="11" r="5"/><circle cx="16" cy="8" r="6"/><circle cx="24" cy="11" r="5"/><rect x="3" y="25" width="26" height="2"/></svg></span></div>
  <h3>Ethno Botanical<br>Surveys</h3>
  <p>At vero eos et accusamus et iusto odio dignissimos ducimus qui blanditiis praesentium</p>
</div>

<section class="abs band"></section>
<svg class="abs" style="left:320px;top:672px" width="36" height="18" viewBox="0 0 36 18"><path d="M0 0h36L18 18z" fill="#fff"/></svg>

<h2 class="abs section-title about-title">ABOUT</h2>
<svg class="abs" style="left:75px;top:744px" width="16" height="8"><path d="M0 1h16M0 6h16" stroke="#33a6d7" stroke-width="1.2"/></svg>
<div class="abs more-btn">More »</div>
<div class="abs about-text">
  <p>We are accountable for delivering quality, timely, sustainable, discreet, affordable environment services in a professional manner. We are also accountable to the relevant Environmental Legislation and policy including Parliamentary Acts, State and local laws.</p>
  <p>Take the time to explore our website and if the service you require isn't highlighted here don't hesitate to contact us with a brief of the project you have in mind. We have great staff diversity and would be happy to give your project due consideration.</p>
  <p>All photos displayed have been taken by staff on site during property visits.</p>
</div>
<div class="abs about-photo" role="img" aria-label="Photo of a white spider orchid among green grass"></div>

<h2 class="abs section-title projects-title">RECENT PROJECTS</h2>
<svg class="abs" style="left:372px;top:744px" width="16" height="8"><path d="M0 1h16M0 6h16" stroke="#33a6d7" stroke-width="1.2"/></svg>
<div class="abs project" style="top:776px">
  <div class="project-photo" role="img" aria-label="Photo of purple wildflowers" style="background:linear-gradient(135deg,#6b8a3a,#9a5cc0 50%,#4d6b2a)"></div>
  <p>Vestibulum sit amet mi tristique, interdum ligula id, pulvinar est.</p>
</div>
<div class="abs project" style="top:858px">
  <div class="project-photo" role="img" aria-label="Photo of orange pea flowers" style="background:linear-gradient(135deg,#3e5a23,#e08a2a 45%,#c64a2a 60%,#4a6a2a)"></div>
  <p>Nulla vitae ligula euismod, blandit ante sagittis, consectetur magna.</p>
</div>
<div class="abs project" style="top:942px">
  <div class="project-photo" role="img" aria-label="Photo of a pale pink orchid" style="background:linear-gradient(135deg,#e3d4d8,#c9aab7 50%,#e8e2e0)"></div>
  <p>Maecenas eu orci ultricies neque congue mollis sit amet eu turpis.</p>
</div>
<svg class="abs" style="left:404px;top:961px" width="22" height="22" viewBox="0 0 22 22"><circle cx="11" cy="11" r="11" fill="#333" opacity=".75"/><circle cx="10" cy="10" r="4" fill="none" stroke="#fff" stroke-width="1.5"/><path d="M13 13l3.5 3.5" stroke="#fff" stroke-width="1.5"/></svg>

<footer class="abs footer"></footer>
<div class="abs footer-brand"><div class="brand-mark"></div><div class="name">Marri Vale Ecoservices</div></div>
<div class="abs copyright">© Copyright - Marri Vale Ecoservices</div>

<div class="abs f-col" style="left:233px">
  <h4>Navigation</h4>
  <ul><li>Home</li><li style="color:#fff;text-decoration:underline;line-height:10px;margin:2px 0">Environmental Planning<br>and Management</li><li style="line-height:10px;margin:2px 0">Revegetation and<br>Regeneration Implementation</li><li>About Us</li><li>Contact</li></ul>
</div>
<div class="abs f-col" style="left:364px">
  <h4>About Us</h4>
  <div class="info"><b>Vale,</b> 6285 Karridale Road 42</div>
  <div class="info" style="margin-top:16px"><b>Phone:</b> (+61) 8 9000 4417</div>
  <div class="info"><b>Email:</b> hello@marrivale-eco.net</div>
</div>
<div class="abs f-col" style="left:512px">
  <h4>Education</h4>
  <ul><li>Marine Activities</li><li>River/Estuary</li><li>Bush Activities</li><li>AusVELS, VET,VCAL and VCE</li><li>School holiday programs</li><li>Cape Point Lighthouse Tour</li></ul>
</div>

</body>
</html>
```